Webdesign für einen gemeinnützigen Verein
Zielgruppe
Merovalien e. V. ist ein gemeinnütziger Verein der sich auf die Fahne geschrieben hat sich für Inklusive und Vielfalt einzusetzen. Wir unterstützen Menschen mit Behinderung beim selbstbestimmten Leben und helfen auch bei Anträgen etc. Des weiteren helfen wir Firmen, Vereinen und stonstigen Organisationen Ihre Inhalte und Auftritte barrierefrei zu gestallten. Wir Testen Apps und Websites und geben hier Feedback.
Aufgabenstellung
Wir möchten ein WordPress Theme das responsiv und persistent ist. Wir möchten die Inhalte später mit WordPress Einpflege und die Seite managen.
Unser Corporate Design steht bereits und beinhaltet die Pride Farben und sollte somit in einem hellen und dunklen Design umgesetzt werden. Wir möchten hier 2 Varianten vom Homepage Design (Darkmode)
Poppins ist unsere Schriftart für Textinhalte
Google Fonds möchten wir nicht nutzen
Passende Social Media Icons

```html
<!DOCTYPE html>
<html lang="de">
<head>
<meta charset="utf-8">
<title>Merovalien e. V. – Homepage Darkmode</title>
<link href="https://fonts.googleapis.com/css2?family=Poppins:wght@300;400;500;600;700&display=swap" rel="stylesheet">
<style>
:root{
  --board:#ececec;
  --navy:#111838;
  --navy-2:#151c40;
  --purple:#4c1675;
  --purple-mid:#2d1756;
  --violet:#7b3fc4;
  --emblem:#5a1f8c;
  --white:#ffffff;
  --muted:#c9c9d8;
  --link:#6f7bd8;
  --rainbow:linear-gradient(90deg,#e53935,#fb8c00,#fdd835,#43a047,#1e88e5,#8e24aa);
  --hero-grad:linear-gradient(100deg,var(--purple) 0%,var(--purple-mid) 45%,var(--navy) 100%);
}
*{box-sizing:border-box;margin:0;padding:0}
html,body{width:1200px;height:4227px;overflow:hidden;background:var(--board)}
body{font-family:'Poppins',sans-serif;color:var(--white);position:relative}
.abs{position:absolute}
.column{position:absolute}
.column--desktop{left:338px;top:44px;width:819px}
.column--mobile{left:43px;top:44px;width:259px}
.section{position:absolute;left:0;width:100%;overflow:hidden}
.bg-hero{background:var(--hero-grad)}
.bg-navy{background:var(--navy)}
.bg-navy2{background:var(--navy-2)}
.nav{position:absolute;left:0;top:0;width:100%;height:59px;display:flex;align-items:center;padding:0 49px;background:var(--navy);border-top:1px solid #222a50;z-index:2}
.brand{display:flex;align-items:center;gap:8px;font-size:12px;font-weight:500;letter-spacing:.3px}
.brand-mark{width:26px;height:26px;border-radius:50%;background:var(--violet)}
.menu{margin-left:auto;display:flex;align-items:center;gap:20px;font-size:10px}
.menu .active{background:var(--rainbow);padding:1px 9px;border-radius:9px}
.toggle{width:42px;height:18px;border-radius:9px;background:var(--violet);position:relative;margin-left:18px}
.toggle::before{content:"";position:absolute;left:5px;top:6px;width:6px;height:6px;border-radius:50%;background:#fff}
.toggle::after{content:"";position:absolute;right:4px;top:3px;width:12px;height:12px;border-radius:50%;background:#fff}
.burger{margin-left:auto;width:20px;height:20px;border-radius:4px;background:var(--rainbow)}
.splash-mark{width:52px;height:52px;border-radius:50%;background:var(--violet)}
.splash-line{height:3px;background:var(--rainbow);border-radius:2px}
.emblem{border-radius:50%;background:var(--emblem)}
.socials{display:flex;gap:18px}
.socials span{width:12px;height:12px;border-radius:50%;border:2px solid #fff}
.btn{display:inline-block;background:#fff;color:var(--purple);font-size:9px;font-weight:600;padding:5px 10px;border-radius:10px;letter-spacing:.3px}
.btn--sm{font-size:6.5px;padding:4px 8px}
.title{font-weight:600;text-align:center;width:100%;letter-spacing:.5px}
.copy{color:var(--muted);font-weight:300}
.copy b{color:#fff;font-weight:600}
.media{border-radius:4px}
.media--photo{background:linear-gradient(135deg,#8b8f9c,#d2d4da 60%,#5e6675)}
.media--illu{background:linear-gradient(120deg,#b4a6f2,#7c5ad6);border-radius:40% 50% 45% 55%}
.media--people{background:linear-gradient(90deg,#5b3a8a,#a5789a 50%,#6a4096)}
.media--portrait{background:linear-gradient(180deg,#a7a7a7,#3d3d3d);border-radius:12px}
.media--map{background:linear-gradient(135deg,#eef0ec,#dfe4dc);border-radius:10px}
.up{width:22px;height:22px;border-radius:50%;border:1.5px solid #fff;display:flex;align-items:center;justify-content:center}
.arrow{width:8px;height:8px;border-left:1.5px solid #fff;border-bottom:1.5px solid #fff}
.quote-mark{font-size:60px;font-weight:700;color:rgba(255,255,255,.25);line-height:1}
.name{text-align:center;font-weight:600;line-height:1.35}
.partner{height:14px;border-radius:3px;background:rgba(255,255,255,.45)}
.footer-brand{font-size:17px;font-weight:600;letter-spacing:1px}
.foot{font-size:9.5px;line-height:1.8;color:#dcdcea;font-weight:300}
.input{height:12px;border-radius:3px;background:#9a9aac;font-size:7px;color:#eee;padding-left:4px;line-height:12px}
.rainbow-bar{background:var(--rainbow);text-align:center;font-size:7.5px}
</style>
</head>
<body>

<!-- ================= DESKTOP ================= -->
<div class="column column--desktop">

  <section class="section bg-hero" style="top:0;height:460px">
    <div class="abs splash-mark" style="left:383px;top:201px"></div>
    <div class="abs splash-line" style="left:340px;top:282px;width:139px"></div>
  </section>

  <section class="section bg-hero" style="top:460px;height:461px">
    <nav class="nav">
      <div class="brand"><span class="brand-mark"></span>MEROVALIEN</div>
      <div class="menu"><span class="active">Home</span><span>Verein</span><span>Projekte</span><span>Team</span><span>Blog</span><span>Wir im Netz</span><span>Kontakt</span><span class="toggle"></span></div>
    </nav>
    <div class="abs emblem" style="left:520px;top:130px;width:225px;height:225px"></div>
    <div class="abs socials" style="left:637px;top:80px"><span></span><span></span><span></span><span></span><span></span></div>
    <div class="abs" style="left:110px;top:150px;font-size:20px;line-height:31px">
      <div style="font-weight:600">Merovalien<span style="font-weight:300">|</span></div>
      <div>Verein zur Förderung der</div>
      <div><b>Kommunikation</b> und <b>Inklusion</b></div>
      <div>für ein selbstbestimmtes Leben e. V.</div>
    </div>
    <div class="abs" style="left:48px;top:225px"><div class="arrow" style="transform:rotate(45deg)"></div></div>
    <div class="abs" style="left:760px;top:225px"><div class="arrow" style="transform:rotate(-135deg)"></div></div>
    <span class="abs btn" style="left:112px;top:292px">MEHR ERFAHREN</span>
    <div class="abs quote-mark" style="left:110px;top:330px">“</div>
    <div class="abs" style="left:152px;top:383px;font-size:14px;font-weight:300">Sprache ist der Schlüssel zur Inklusion : Merovalien öffnet Türen</div>
    <div class="abs quote-mark" style="left:660px;top:398px">”</div>
  </section>

  <section class="section bg-navy" style="top:921px;height:460px">
    <nav class="nav">
      <div class="brand"><span class="brand-mark"></span>MEROVALIEN</div>
      <div class="menu"><span class="active">Home</span><span>Verein</span><span>Projekte</span><span>Team</span><span>Blog</span><span>Wir im Netz</span><span>Kontakt</span><span class="toggle"></span></div>
    </nav>
    <h2 class="abs title" style="top:78px;font-size:21px">WAS MACHT UNS AUS?</h2>
    <p class="abs copy" style="left:110px;top:128px;width:318px;font-size:10.2px;line-height:1.45"><b>Merovalien</b> beschäftigt sich mit der Förderung von selbstbestimmtem Leben von Menschen mit Behinderungen sowie der Schaffung von Barrierefreiheit bei digitalen Medien.<br>Ein weiterer Fokus liegt auf der Verbesserung der Kommunikation zwischen Menschen, Institutionen und Organisationen, insbesondere zwischen Menschen mit und ohne Behinderungen.<br>Ziel ist es, Barrieren zu beseitigen und eine inklusive Gesellschaft zu schaffen, in der alle Menschen gleichermaßen teilhaben können.<br>Die Förderung von Empowerment und die Stärkung der Stimmen von Menschen mit Behinderungen sind ebenfalls wichtige Bestandteile von Merovalien. Durch die Förderung einer offenen und vielfältigen Kommunikation, die Schaffung von barrierefreien Angeboten und die Verbreitung von Wissen und Informationen über Behinderungen und Inklusion kann eine inklusive Gesellschaft erreicht werden, in der jeder Mensch gleichberechtigt und selbstbestimmt leben kann.</p>
    <div class="abs media media--illu" role="img" aria-label="Illustration: Gruppe von Menschen, eine Person im Rollstuhl, zwischen Pflanzen" style="left:425px;top:144px;width:312px;height:196px"></div>
    <span class="abs btn" style="left:540px;top:373px">MEHR ERFAHREN</span>
    <div class="abs up" style="left:726px;top:419px"><div class="arrow" style="transform:rotate(135deg);margin-top:3px"></div></div>
  </section>

  <section class="section bg-navy" style="top:1381px;height:462px">
    <nav class="nav">
      <div class="brand"><span class="brand-mark"></span>MEROVALIEN</div>
      <div class="menu"><span class="active">Home</span><span>Verein</span><span>Projekte</span><span>Team</span><span>Blog</span><span>Wir im Netz</span><span>Kontakt</span><span class="toggle"></span></div>
    </nav>
    <h2 class="abs title" style="top:78px;font-size:21px">WAS MACHEN WIR?</h2>
    <div class="abs media media--photo" role="img" aria-label="Foto: Podcast-Aufnahme mit Gästen am Tisch" style="left:92px;top:136px;width:159px;height:104px"></div>
    <div class="abs media media--photo" role="img" aria-label="Foto: Vortrag im Büro mit Person im Rollstuhl" style="left:92px;top:272px;width:159px;height:105px"></div>
    <p class="abs copy" style="left:296px;top:134px;width:474px;font-size:9.5px;line-height:1.8;text-align:justify">Unsere zahlreichen Podcast behandeln die Themen wofür wir stehen was uns ausmacht. Wir möchten über dieses Medium mit Sprache zeigen wie wichtig die Kommunikation ist. Wir wollen aufklären und Wissen vermitteln. Ob zu gesellschaftlichen Themen im Bereich der Inklusion oder Barrierefreiheit in digitalen Medien. Egal ob Technik wie SmartHome oder Gaming.</p>
    <span class="abs btn" style="left:296px;top:210px">MEHR ERFAHREN</span>
    <p class="abs copy" style="left:296px;top:262px;width:474px;font-size:9.5px;line-height:1.8;text-align:justify"><b>Vortrag und Kommunikationsprojekt zum Persönlichen Budget</b><br>Assistenz für Menschen mit Behinderungen ist wichtig um ein selbstbestimmtes Leben zu gestalten. Dieser Vortrag führte im Anschluss zu einer Community über die sich Betroffene und Beratende Personen austauschen. Höre jetzt den Vortrag und trete der Community bei.</p>
    <div class="abs" style="left:296px;top:335px;font-size:9px;color:var(--link)">…mehr erfahren unter seite zu den infos und Vortrag Community etc.</div>
    <span class="abs btn" style="left:358px;top:381px">WEITERE PROJEKTE</span>
    <div class="abs up" style="left:726px;top:420px"><div class="arrow" style="transform:rotate(135deg);margin-top:3px"></div></div>
  </section>

  <section class="section bg-navy" style="top:1843px;height:460px">
    <nav class="nav">
      <div class="brand"><span class="brand-mark"></span>MEROVALIEN</div>
      <div class="menu"><span class="active">Home</span><span>Verein</span><span>Projekte</span><span>Team</span><span>Blog</span><span>Wir im Netz</span><span>Kontakt</span><span class="toggle"></span></div>
    </nav>
    <div class="abs media media--people" role="img" aria-label="Foto: lachende Gruppe junger Menschen" style="left:154px;top:66px;width:511px;height:102px;border-radius:10px"></div>
    <div class="abs" style="left:154px;top:78px;width:511px;text-align:center;font-size:21px;font-weight:600;line-height:1.45">WER SIND WIR?<br><span style="font-weight:400;letter-spacing:.6px">“Gemeinsam aktiv für eine inklusive Zukunft”</span></div>
    <div class="abs media media--portrait" role="img" aria-label="Porträtfoto Vorstandsmitglied" style="left:154px;top:223px;width:103px;height:138px"></div>
    <div class="abs media media--portrait" role="img" aria-label="Porträtfoto Vorstandsmitglied" style="left:356px;top:223px;width:104px;height:138px"></div>
    <div class="abs media media--portrait" role="img" aria-label="Porträtfoto Vorstandsmitglied" style="left:560px;top:223px;width:104px;height:138px"></div>
    <div class="abs name" style="left:130px;top:372px;width:150px;font-size:9.5px">MALIK ORHAN<br>VORSTAND</div>
    <div class="abs name" style="left:333px;top:372px;width:150px;font-size:9.5px">JANA WEILER<br>VORSTAND</div>
    <div class="abs name" style="left:537px;top:372px;width:150px;font-size:9.5px">TOBIAS BRANDNER<br>VORSTAND</div>
    <div class="abs up" style="left:726px;top:418px"><div class="arrow" style="transform:rotate(135deg);margin-top:3px"></div></div>
  </section>

  <section class="section" style="top:2303px;height:699px;background:linear-gradient(180deg,var(--purple) 0%,var(--navy) 38%)">
    <h2 class="abs title" style="top:24px;font-size:21px">MIT DIR EIN GRÖßERES WIR</h2>
    <p class="abs" style="left:60px;top:70px;width:700px;text-align:center;font-size:9.8px;line-height:1.65;font-weight:300">Willst du dich für eine inklusive und barrierefreie Gesellschaft einsetzen und<br>Menschen mit Behinderungen dabei helfen, ein selbstbestimmtes Leben zu führen?<br>Dann bist du bei unserem Verein Merovalien e. V. genau richtig! Gemeinsam möchten wir Barrieren abbauen,<br>Vorurteile überwinden und eine vielfältige und offene Kommunikation fördern.<br>Wir suchen motivierte Menschen, die sich für eine bessere Welt einsetzen möchten und aktiv etwas bewirken wollen.<br>Werde Teil unserer Community und trage dazu bei, dass Inklusion und Barrierefreiheit in unserer Gesellschaft gelebt werden!<br>Meide dich jetzt bei uns und werde Teil unserer Bewegung!</p>
    <span class="abs btn" style="left:359px;top:197px;background:var(--violet);color:#fff">MEHR ERFAHREN</span>
    <div class="abs partner" style="left:49px;top:264px;width:92px"></div>
    <div class="abs partner" style="left:172px;top:264px;width:122px"></div>
    <div class="abs partner" style="left:318px;top:264px;width:92px"></div>
    <div class="abs partner" style="left:448px;top:264px;width:82px"></div>
    <div class="abs partner" style="left:565px;top:264px;width:82px"></div>
    <div class="abs partner" style="left:680px;top:264px;width:90px"></div>
    <div class="abs media media--map" role="img" aria-label="Stadtplan mit Standortmarkierung des Vereins" style="left:49px;top:313px;width:721px;height:188px"></div>
    <div class="abs footer-brand" style="left:49px;top:538px">MEROVALIEN</div>
    <div class="abs foot" style="left:49px;top:570px">Merovalien e. V.<br>c/o Brandner Lindenweg 14<br>10115 Berlin<br>Tel.&nbsp;&nbsp;&nbsp;&nbsp;&nbsp;: +49 (0) 30 5550 1120<br>Fax.&nbsp;&nbsp;&nbsp;&nbsp;: +49 (0) 30 5550 1121<br>E-Mail&nbsp;: info@merovalien.de</div>
    <div class="abs foot" style="left:356px;top:588px">Service<br>Blog<br>Privacy &amp; Policy<br>Sitemap<br>Barrierefreiheit</div>
    <div class="abs" style="left:584px;top:538px;width:186px;font-size:9px;line-height:1.2;text-align:center">—— Verein zur Förderung der ——<br>Kommunikation und Inklusion<br>für ein selbstbestimmtes Leben e. V.</div>
    <div class="abs input" style="left:584px;top:584px;width:141px">email</div>
    <div class="abs foot" style="left:584px;top:598px"><span style="color:var(--link)">Abonnieren Sie unseren Newsletter</span><br>Impressum<br>Datenschutzerklärung<br>Cookie-Richtlinie</div>
    <div class="abs up" style="left:726px;top:640px"><div class="arrow" style="transform:rotate(135deg);margin-top:3px"></div></div>
    <div class="abs rainbow-bar" style="left:0;top:680px;width:100%;height:19px;line-height:19px">© 2023, <b>MEROVALIEN</b> All rights reserved</div>
  </section>
</div>

<!-- ================= MOBILE ================= -->
<div class="column column--mobile">

  <section class="section bg-hero" style="top:0;height:460px">
    <div class="abs splash-mark" style="left:104px;top:201px"></div>
    <div class="abs splash-line" style="left:60px;top:282px;width:139px"></div>
  </section>

  <section class="section bg-hero" style="top:460px;height:461px">
    <nav class="nav" style="padding:0 16px">
      <div class="brand" style="font-size:10px"><span class="brand-mark" style="width:22px;height:22px"></span>MEROVALIEN</div>
      <span class="burger"></span>
    </nav>
    <div class="abs emblem" style="left:30px;top:160px;width:200px;height:200px;opacity:.45"></div>
    <div class="abs socials" style="left:69px;top:91px;gap:18px"><span></span><span></span><span></span><span></span><span></span></div>
    <div class="abs" style="left:0;top:128px;width:100%;text-align:center;font-size:17px;line-height:1.6">
      <div style="font-weight:600">Merovalien<span style="font-weight:300">|</span></div>
      <div>Verein zur Förderung</div>
      <div>der <b>Kommunikation</b></div>
      <div>und <b>Inklusion</b> für ein</div>
      <div>selbstbestimmtes</div>
      <div>Leben e. V.</div>
    </div>
    <span class="abs btn btn--sm" style="left:88px;top:308px">MEHR ERFAHREN</span>
    <div class="abs quote-mark" style="left:26px;top:338px;font-size:38px">“</div>
    <div class="abs" style="left:0;top:356px;width:100%;text-align:center;font-size:8.5px;line-height:1.9;font-weight:300">Sprache ist der Schlüssel zur Inklusion :<br>Merovalien öffnet Türen</div>
    <div class="abs quote-mark" style="left:206px;top:368px;font-size:38px">”</div>
    <div class="abs" style="left:96px;top:430px"><div class="arrow" style="transform:rotate(45deg)"></div></div>
    <div class="abs" style="left:158px;top:430px"><div class="arrow" style="transform:rotate(-135deg)"></div></div>
  </section>

  <section class="section bg-navy" style="top:921px;height:460px">
    <h2 class="abs title" style="top:18px;font-size:14px">WAS MACHT UNS AUS?</h2>
    <div class="abs media media--illu" role="img" aria-label="Illustration: Gruppe von Menschen, eine Person im Rollstuhl" style="left:47px;top:44px;width:156px;height:86px"></div>
    <p class="abs copy" style="left:29px;top:150px;width:200px;font-size:7px;line-height:1.4"><b>Merovalien</b> beschäftigt sich mit der Förderung von selbstbestimmtem Leben von Menschen mit Behinderungen sowie der Schaffung von Barrierefreiheit bei digitalen Medien.<br>Ein weiterer Fokus liegt auf der Verbesserung der Kommunikation zwischen Menschen, Institutionen und Organisationen, insbesondere zwischen Menschen mit und ohne Behinderungen.<br>Ziel ist es, Barrieren zu beseitigen und eine inklusive Gesellschaft zu schaffen, in der alle Menschen gleichermaßen teilhaben können. Die Förderung von Empowerment und die Stärkung der Stimmen von Menschen mit Behinderungen sind ebenfalls wichtige Bestandteile von Merovalien. Durch die Förderung einer offenen und vielfältigen Kommunikation, die Schaffung von barrierefreien Angeboten und die Verbreitung von Wissen und Informationen über Behinderungen und Inklusion kann eine inklusive Gesellschaft erreicht werden, in der jeder Mensch gleichberechtigt und selbstbestimmt leben kann.</p>
    <span class="abs btn btn--sm" style="left:90px;top:415px">MEHR ERFAHREN</span>
  </section>

  <section class="section bg-navy" style="top:1381px;height:462px;border-top:1px solid #222a50">
    <h2 class="abs title" style="top:10px;font-size:14px">WAS MACHEN WIR?</h2>
    <div class="abs media media--photo" role="img" aria-label="Foto: Podcast-Aufnahme mit Gästen" style="left:57px;top:29px;width:145px;height:97px"></div>
    <p class="abs copy" style="left:20px;top:133px;width:219px;font-size:6.3px;line-height:1.35;text-align:center">Unsere zahlreichen Podcast behandeln die Themen wofür wir stehen was uns ausmacht. Wir möchten über dieses Medium mit Sprache zeigen wie wichtig die Kommunikation ist. Wir wollen aufklären und Wissen vermitteln. Ob zu gesellschaftlichen Themen im Bereich der Inklusion oder Barrierefreiheit in digitalen Medien. Egal ob Technik wie SmartHome oder Gaming.</p>
    <span class="abs btn btn--sm" style="left:90px;top:210px">MEHR ERFAHREN</span>
    <div class="abs media media--photo" role="img" aria-label="Foto: Vortrag im Büro mit Person im Rollstuhl" style="left:57px;top:229px;width:145px;height:95px"></div>
    <p class="abs copy" style="left:16px;top:330px;width:227px;font-size:6.3px;line-height:1.35;text-align:justify"><b>Vortrag und Kommunikationsprojekt zum Persönlichen Budget</b> Assistenz für Menschen mit Behinderungen ist wichtig um ein selbstbestimmtes Leben zu gestalten. Dieser Vortrag führte im Anschluss zu einer Community über die sich Betroffene und Beratende Personen austauschen. Höre jetzt den Vortrag und trete der Community bei.<br><span style="color:var(--link)">…mehr erfahren unter seite zu den infos und Vortrag Community etc.</span></p>
    <span class="abs btn btn--sm" style="left:82px;top:436px">WEITERE PROJEKTE</span>
  </section>

  <section class="section bg-navy" style="top:1843px;height:460px">
    <div class="abs media media--people" role="img" aria-label="Foto: lachende Gruppe junger Menschen" style="left:14px;top:25px;width:229px;height:41px;border-radius:5px"></div>
    <div class="abs" style="left:14px;top:28px;width:229px;text-align:center;font-size:12.5px;font-weight:600;line-height:1.2">WER SIND WIR?<br><span style="font-size:7.5px;font-weight:400">“Gemeinsam aktiv für eine inklusive Zukunft”</span></div>
    <div class="abs media media--portrait" role="img" aria-label="Porträtfoto Vorstandsmitglied" style="left:49px;top:128px;width:161px;height:212px;border-radius:18px"></div>
    <div class="abs name" style="left:0;top:356px;width:100%;font-size:14.5px">MALIK ORHAN<br>VORSTAND</div>
  </section>

  <section class="section bg-navy2" style="top:2303px;height:460px">
    <div class="abs media media--portrait" role="img" aria-label="Porträtfoto Vorstandsmitglied" style="left:49px;top:100px;width:161px;height:212px;border-radius:18px"></div>
    <div class="abs name" style="left:0;top:327px;width:100%;font-size:14.5px">JANA WEILER<br>VORSTAND</div>
  </section>

  <section class="section bg-navy" style="top:2763px;height:459px">
    <div class="abs media media--portrait" role="img" aria-label="Porträtfoto Vorstandsmitglied" style="left:49px;top:99px;width:161px;height:212px;border-radius:18px"></div>
    <div class="abs name" style="left:0;top:329px;width:100%;font-size:14.5px">TOBIAS BRANDNER<br>VORSTAND</div>
  </section>

  <section class="section" style="top:3222px;height:925px;background:linear-gradient(180deg,var(--purple) 0%,var(--navy) 30%)">
    <h2 class="abs title" style="top:25px;font-size:14px">MIT DIR EIN GRÖßERES WIR</h2>
    <p class="abs" style="left:14px;top:62px;width:231px;text-align:center;font-size:6.3px;line-height:1.55;font-weight:300">Willst du dich für eine inklusive und barrierefreie Gesellschaft einsetzen und Menschen mit Behinderungen dabei helfen, ein selbstbestimmtes Leben zu führen? Dann bist du bei unserem Verein Merovalien e. V. genau richtig! Gemeinsam möchten wir Barrieren abbauen, Vorurteile überwinden und eine vielfältige und offene Kommunikation fördern. Wir suchen motivierte Menschen, die sich für eine bessere Welt einsetzen möchten und aktiv etwas bewirken wollen. Werde Teil unserer Community und trage dazu bei, dass Inklusion und Barrierefreiheit in unserer Gesellschaft gelebt werden! Meide dich jetzt bei uns und werde Teil unserer Bewegung!</p>
    <span class="abs btn btn--sm" style="left:82px;top:246px;background:var(--violet);color:#fff">MEHR ERFAHREN</span>
    <div class="abs partner" style="left:14px;top:284px;width:86px"></div>
    <div class="abs partner" style="left:138px;top:284px;width:107px"></div>
    <div class="abs partner" style="left:14px;top:316px;width:86px"></div>
    <div class="abs partner" style="left:150px;top:316px;width:70px"></div>
    <div class="abs partner" style="left:14px;top:348px;width:82px"></div>
    <div class="abs partner" style="left:140px;top:348px;width:88px"></div>
    <div class="abs media media--map" role="img" aria-label="Stadtplan mit Standortmarkierung des Vereins" style="left:14px;top:405px;width:229px;height:79px;border-radius:4px"></div>
    <div class="abs footer-brand" style="left:0;top:546px;width:100%;text-align:center">MEROVALIEN</div>
    <div class="abs" style="left:0;top:573px;width:100%;text-align:center;font-size:7.5px;line-height:1.2">—— Verein zur Förderung der ——<br>Kommunikation und Inklusion<br>für ein selbstbestimmtes Leben e. V.</div>
    <div class="abs foot" style="left:45px;top:614px">Merovalien e. V.<br>c/o Brandner Lindenweg 14<br>10115 Berlin<br>Tel.&nbsp;&nbsp;&nbsp;&nbsp;&nbsp;: +49 (0) 30 5550 1120<br>Fax.&nbsp;&nbsp;&nbsp;&nbsp;: +49 (0) 30 5550 1121<br>E-Mail&nbsp;: info@merovalien.de<br>Service<br>Blog<br>Privacy &amp; Policy<br>Sitemap<br>Barrierefreiheit</div>
    <div class="abs input" style="left:45px;top:832px;width:97px">email</div>
    <div class="abs foot" style="left:45px;top:846px"><span style="color:var(--link)">Abonnieren Sie unseren Newsletter</span><br>Impressum<br>Datenschutzerklärung<br>Cookie-Richtlinie</div>
  </section>
  <div class="abs rainbow-bar" style="left:0;top:4124px;width:259px;height:19px;line-height:19px;font-size:6.5px">© 2023, <b>MEROVALIEN</b> All rights reserved</div>
</div>

</body>
</html>
```